Business Card Design Project

I need a business card design for an Organic drive thru coffee kiosk. We will serve organic coffee, teas & smoothies and will serve healthy breakfast food/snacks for people on the go.
I want the card to have 2-3 colors max (earthy colors like browns, greens and so on).
I have attached the logo I want used and would love to play off the theme of "balance."
Include:
Tidy-Kettle Coffee
address: 4820 Gorvin Ct. Raleigh, NC 27583
phone: 919-731-4062
website: www.tidy-kettle.com (website is not up yet but still include it on card)
email: Rosalind@tidy-kettle.com
I want one of the following sayings somewhere on the card (the front or back is fine):
"Sip & Snack Tidy, on the run!"
"Break the fast with Tidy-Kettle"
Maybe on the back list what we offer:
-Organic coffee, espresso & tea
-Blendora smoothies & protein shakes
-Zesty Pour (100% fresh local fruit and veggies)
-Tender Nibs

```html
<!DOCTYPE html>
<html lang="en">
<head>
<meta charset="utf-8">
<title>Tidy-Kettle Coffee – Business Card</title>
<link rel="stylesheet" href="https://fonts.googleapis.com/css2?family=Play:wght@400;700&family=Rye&display=swap">
<style>
  :root {
    --page: #ffffff;
    --card: #fbfbdc;
    --disc: #d6cfab;
    --leaf: #3a9a12;
    --ink: #6b1e12;
    --quote: #7a2614;
    --name: #2a1a12;
  }
  * { box-sizing: border-box; margin: 0; padding: 0; }
  html, body {
    width: 1200px; height: 1000px; overflow: hidden;
    background: var(--page);
  }
  .canvas { position: relative; width: 1200px; height: 1000px; }
  .card {
    position: absolute;
    width: 664px; height: 397px;
    background: var(--card);
    overflow: hidden;
    box-shadow: 0 10px 22px rgba(0,0,0,.55);
    font-family: "Play", sans-serif;
    color: var(--ink);
  }
  .card-front { left: 32px; top: 58px; }
  .card-back  { left: 464px; top: 536px; }

  .emblem { position: absolute; inset: 0; width: 664px; height: 397px; }
  .emblem .quote {
    font-family: "Rye", serif;
    font-size: 18px;
    fill: var(--quote);
  }
  .emblem .brand-name {
    font-family: "Play", sans-serif;
    font-weight: 400;
    font-size: 56px;
    fill: var(--name);
  }

  .address {
    position: absolute; left: 14px; top: 178px;
    font-style: normal;
    font-size: 25px; line-height: 27px;
  }
  .contact {
    position: absolute; left: 12px; top: 318px;
    font-size: 20px; line-height: 23px;
    border-collapse: collapse;
  }
  .contact td { padding: 0; vertical-align: top; }
  .contact .label { padding-right: 8px; }

  .offerings {
    position: absolute; left: 14px; top: 64px;
    list-style: none;
    font-size: 26px; font-weight: 700; letter-spacing: 1px;
  }
  .offerings li {
    display: flex; align-items: flex-end;
    height: 58px;
    white-space: nowrap;
  }
  .offerings svg { width: 30px; height: 34px; flex: none; margin-right: 4px; fill: var(--ink); }
</style>
</head>
<body>
<div class="canvas">

  <section class="card card-front">
    <svg class="emblem" viewBox="0 0 664 397">
      <circle cx="458" cy="198" r="199" fill="var(--leaf)"/>
      <circle cx="466" cy="198" r="199" fill="var(--disc)"/>
      <defs>
        <path id="arc-top" d="M 306 112 A 205 205 0 0 1 626 112"/>
        <path id="arc-bottom" d="M 323 322 A 245 245 0 0 0 609 322"/>
      </defs>
      <text class="quote"><textPath href="#arc-top" startOffset="50%" text-anchor="middle">"Break the fast with Tidy-Kettle"</textPath></text>
      <text class="quote"><textPath href="#arc-bottom" startOffset="50%" text-anchor="middle">"Sip &amp; Snack Tidy, on the run!"</textPath></text>
      <circle cx="466" cy="150" r="30" fill="var(--quote)"/>
      <text class="brand-name" x="466" y="262" text-anchor="middle">Tidy-Kettle</text>
    </svg>

    <address class="address">
      Tidy-Kettle Coffee<br>
      4820 Gorvin Ct.<br>
      Raleigh,<br>
      NC 27583
    </address>

    <table class="contact">
      <tr><td class="label">Ph:</td><td>919-731-4062</td></tr>
      <tr><td class="label">Web:</td><td>www.tidy-kettle.com</td></tr>
      <tr><td class="label">Email:</td><td>Rosalind@tidy-kettle.com</td></tr>
    </table>
  </section>

  <section class="card card-back">
    <ul class="offerings">
      <li>
        <svg viewBox="0 0 30 34" aria-hidden="true">
          <path d="M3 22 h18 v2 a7 5 0 0 1 -7 5 h-4 a7 5 0 0 1 -7 -5z"/>
          <path d="M21 23 h3 a3 3 0 0 1 0 5 h-3 v-1.5 h3 a1.2 1.2 0 0 0 0 -2 h-3z"/>
          <rect x="1" y="30" width="24" height="2" rx="1"/>
        </svg>
        Organic coffee, espresso &amp; tea
      </li>
      <li>
        <svg viewBox="0 0 30 34" aria-hidden="true">
          <path d="M4 12 h16 l-3 9 h-10z"/>
          <rect x="11" y="20" width="3" height="9"/>
          <rect x="7" y="29" width="11" height="3" rx="1"/>
          <path d="M14 12 l6 -8 h5 v1.5 h-4.3 l-5.2 6.5z"/>
          <circle cx="5" cy="10" r="3"/>
        </svg>
        Blendora smoothies &amp; protein shakes
      </li>
      <li>
        <svg viewBox="0 0 30 34" aria-hidden="true">
          <path d="M4 12 h16 l-3 9 h-10z"/>
          <rect x="11" y="20" width="3" height="9"/>
          <rect x="7" y="29" width="11" height="3" rx="1"/>
          <path d="M14 12 l6 -8 h5 v1.5 h-4.3 l-5.2 6.5z"/>
          <circle cx="5" cy="10" r="3"/>
        </svg>
        Zesty Pour (100% fresh local fruit and veggies)
      </li>
      <li>
        <svg viewBox="0 0 30 34" aria-hidden="true">
          <path d="M10 0 h1 v7 h1 v-7 h1 v7 h1 v-7 h1 v8 a3 3 0 0 1 -2 3 v23 h-2 v-23 a3 3 0 0 1 -2 -3z"/>
        </svg>
        Tender Nibs
      </li>
    </ul>
  </section>

</div>
</body>
</html>
```